Plakat-Design für Unternehmer- und Marktbund
Zielgruppe
Der Unternehmer- und Marktbund ist ein Verein - Zusammenschluss von Gewerbetreibenden. Im Prinzip wie die Organisation Kreis der Freischaffenden.
Aufgabenstellung
An den Ortseingängen der Gemeinde Wendelsried stehen Ortsinformationstafeln welche immer für den Aufzug von aktuellen Veranstaltungen genutzt werden. Dies sind quasi Stahlträger auf welche Plakate aufgezogen werden. Bisher wurden diese immer wieder abgebaut und aufgebaut. Ziel ist es jetzt, dass die das ganze Jahr über stehen - was nicht so schön aussieht. Deswegen soll hier quasi ein Plakat aufgezogen werden, welches genutzt wird, wenn keine Veranstaltung ansteht.
Auf dem Plakat soll zu sehen sein:
- Logo Gemeinde Wendelsried
- Logo UMB Wendelsried
- Webseite www.umb-wendelsried.de und von der Gemeinde www.wendelsried.de
- Slogan 'Ein starkes Team' gerne sind wir auch für weitere Ideen offen
Informationen von der Firma welche den Druck ausführt
Die Schilder sind 110cm x 160cm, wenn sie das auf einer Plane(Banner) haben wollen, kommen noch 8 Ösen rein, 2cm vom Rand. Die Grafik sollte am besten auf Originalgröße angelegt werden und abspeichern als PDF.

```html
<!DOCTYPE html>
<html lang="de">
<head>
<meta charset="utf-8">
<title>UMB Wendelsried – Ein starkes Team</title>
<link href="https://fonts.googleapis.com/css2?family=Poppins:ital,wght@0,600;0,700;1,800&display=swap" rel="stylesheet">
<style>
  :root {
    --brand-blue: #3b6a9e;
    --header-bg: #f2f2f3;
    --photo-light: #eef1f5;
    --photo-warm: #b98a6c;
    --brand-red: #a3312b;
    --white: #ffffff;
  }
  html, body {
    margin: 0;
    padding: 0;
    width: 840px;
    height: 1200px;
    overflow: hidden;
    background: var(--white);
  }
  .poster {
    position: relative;
    width: 840px;
    height: 1200px;
    overflow: hidden;
    font-family: "Poppins", sans-serif;
    background: var(--photo-light);
  }
  .header {
    position: absolute;
    left: 0; top: 0;
    width: 840px;
    height: 215px;
    background: var(--header-bg);
  }
  .club-mark {
    position: absolute;
    left: 48px;
    top: 62px;
    width: 490px;
    display: flex;
    align-items: center;
    gap: 20px;
  }
  .club-mark__dot {
    flex: 0 0 auto;
    width: 94px;
    height: 94px;
    border-radius: 50%;
    background: var(--brand-red);
  }
  .club-mark__name {
    color: var(--brand-red);
    font-weight: 700;
    line-height: 1.2;
    white-space: nowrap;
  }
  .club-mark__title {
    display: block;
    font-size: 30px;
  }
  .club-mark__subtitle {
    display: block;
    font-size: 17px;
  }
  .town-badge {
    position: absolute;
    left: 566px;
    top: 52px;
    width: 208px;
    height: 244px;
    background: var(--white);
    border-radius: 0 0 104px 104px;
    display: flex;
    flex-direction: column;
    align-items: center;
    justify-content: center;
    gap: 14px;
    z-index: 2;
  }
  .town-badge__square {
    width: 70px;
    height: 70px;
    background: var(--brand-blue);
  }
  .town-badge__name {
    color: var(--brand-blue);
    font-weight: 700;
    font-size: 20px;
    line-height: 1.2;
    text-align: center;
  }
  .photo-hands {
    position: absolute;
    left: 0; top: 215px;
    width: 840px;
    height: 885px;
    background: radial-gradient(circle at 50% 48%, var(--photo-light) 0 36%, #d8c0ae 52%, var(--photo-warm) 70%, #d9c6b8 100%);
  }
  .slogan {
    position: absolute;
    left: 0;
    top: 452px;
    width: 840px;
    margin: 0;
    text-align: center;
    color: var(--brand-blue);
    font-style: italic;
    font-weight: 800;
    font-size: 122px;
    line-height: 144px;
    letter-spacing: -1px;
  }
  .skyline {
    position: absolute;
    left: 0; top: 1010px;
    width: 840px;
    height: 90px;
    background: linear-gradient(to bottom, rgba(59,106,158,0) 0%, rgba(59,106,158,0.55) 60%, var(--brand-blue) 100%);
  }
  .footer {
    position: absolute;
    left: 0; top: 1100px;
    width: 840px;
    height: 100px;
    background: var(--brand-blue);
  }
  .footer__link {
    position: absolute;
    top: 50px;
    color: var(--white);
    font-weight: 600;
    font-size: 21px;
    line-height: 1;
  }
  .footer__link--club { left: 46px; }
  .footer__link--town { right: 52px; }
</style>
</head>
<body>
  <div class="poster">
    <div class="photo-hands" role="img" aria-label="Foto: viele Hände, die sich gegenseitig an den Handgelenken halten und einen Kreis bilden"></div>

    <header class="header">
      <div class="club-mark">
        <div class="club-mark__dot"></div>
        <div class="club-mark__name">
          <span class="club-mark__title">UMB Wendelsried</span>
          <span class="club-mark__subtitle">Unternehmer- und Marktbund e.V.</span>
        </div>
      </div>
    </header>

    <div class="town-badge">
      <div class="town-badge__square"></div>
      <div class="town-badge__name">Gemeinde<br>Wendelsried</div>
    </div>

    <h1 class="slogan">Ein<br>starkes<br>Team</h1>

    <div class="skyline" role="img" aria-label="Silhouette des Ortes mit Kirchturm, Häusern und Baum"></div>

    <footer class="footer">
      <span class="footer__link footer__link--club">www.umb-wendelsried.de</span>
      <span class="footer__link footer__link--town">www.wendelsried.de</span>
    </footer>
  </div>
</body>
</html>
```